Agricultural Commodities Specialist Needs a Business Card Design

Business owner Rob Hartwell, need a business card design for his company based in Brisbane, Australia called "RH Tradelink Pty Ltd".
Rob is an Agricultural Commodities Specialist:
-Specialising in Domestic and Export of Cotton,Cottonseed and Grains.
-Extensive experience in exporting into Asia especially China.
-Buyers agent for one of China's largest spinning mills.
-Capital raising from foreign investors into Australian agriculture.
-Agricultural marketing strategies for corporate and family farms.
-Importer of niche products from China.
-Array of contacts in agriculture and manufacturing in China.

Rob would like a professional business card with his company name "RH Tradelink" on the front of his business card - with contact details on the back. Preferably black and white colours.

CONTACT DETAILS THAT NEED TO BE INCLUDED:

Rob Hartwell
Mobile: 0431 275 604

Po Box 518
Elm Vale QLD 4187

Email: rob@rhtradelinkco.com
website: www.rhtradelinkc.com

```html
<!DOCTYPE html>
<html lang="en">
<head>
<meta charset="utf-8">
<title>Rob Hartwell — Business Card Back</title>
<link rel="stylesheet" href="https://fonts.googleapis.com/css2?family=Cabin:ital,wght@0,400;0,700;1,400&display=swap">
<style>
  :root {
    --card-bg: #000000;
    --ink: #ffffff;
    --ghost: #3b3737;
  }
  html, body {
    margin: 0;
    padding: 0;
    width: 1200px;
    height: 741px;
    overflow: hidden;
    background: var(--card-bg);
  }
  .card {
    display: block;
    width: 1200px;
    height: 741px;
    font-family: "Cabin", "Gill Sans", sans-serif;
  }
  .name-echo {
    fill: var(--ghost);
    font-weight: 700;
    font-size: 67px;
  }
  .name {
    fill: var(--ink);
    font-weight: 700;
    font-size: 67px;
  }
  .detail {
    fill: var(--ink);
    font-size: 29px;
  }
  .detail--strong { font-weight: 700; }
  .detail--online { font-style: italic; }
</style>
</head>
<body>
<svg class="card" viewBox="0 0 1200 741" xmlns="http://www.w3.org/2000/svg" aria-label="Business card contact details for Rob Hartwell">
  <rect width="1200" height="741" fill="var(--card-bg)"/>

  <g class="name-band">
    <text class="name-echo" x="-5" y="344" textLength="495" lengthAdjust="spacingAndGlyphs">ROB HARTWELL</text>
    <text class="name-echo" x="692" y="344" textLength="495" lengthAdjust="spacingAndGlyphs">ROB HARTWELL</text>
    <text class="name" x="351" y="344" textLength="495" lengthAdjust="spacingAndGlyphs">ROB HARTWELL</text>
  </g>

  <g class="contact">
    <text class="detail detail--strong" x="351" y="414">Mobile: 0431 275 604</text>
    <text class="detail" x="351" y="494">Po Box 518</text>
    <text class="detail" x="351" y="535">Elm Vale QLD 4187</text>
    <text class="detail detail--online" x="351" y="617">Email: rob@rhtradelinkco.com</text>
    <text class="detail detail--online" x="351" y="657">website: www.rhtradelinkc.com</text>
  </g>
</svg>
</body>
</html>
```